Corwith Lodge website redesign

After 8 years of our current site, we're ready to upgrade our site design. We'd like to generally make it more modern and clean and build it on a CMS like joomla for easier future maintenance.

Our hotel is a family-owned bed and breakfast that competes against much larger hotel chains in Aspen with fancier rooms and larger pricetags. Our hotel is priced moderately and features tasteful, uniquely-design rooms.

We are looking for a website that will showcase the uniqueness of our rooms, the history of the Lodge, and the friendliness of our staff.

Here are some other hotel sites we like:

http://www.brackenfoldhouse.example/

http://www.tollerpeakhaus.example/

http://www.quarrowstay.example/

*********

Scope of Work - I'm looking for a design AND build. The website should be built out in Joomla as part of the final deliverable.
Updates

Current website: http://www.corwithlodge.example/

Explanation of what design + build means:

I am looking for not only the design of the site, but also for the homepage and one subpage to be built out as well. I do NOT need the entire site built - only for those two pages to be built and I will retrofit the remainder of the pages.

Target Market(s)

travellers evaluating hotels in Aspen, Colorado.

Industry/Entity Type

Hotel

Requirements
Must have
• Must, must, must be based on a joomla template. "Rotating" large main image as central position on homepage is a must (see example websites mentioned above).

Nice to have
• We have an existing online reservation system. It would be nice to evaluate placing a "widget" on the homepage that integrates to the online reservation page. Similar to that feature that the Bracken Fold website has at the foot of the main image on their homepage.

```html
<!DOCTYPE html>
<html lang="en">
<head>
<meta charset="utf-8">
<title>Corwith Lodge – History of the Lodge</title>
<link rel="stylesheet" href="https://fonts.googleapis.com/css2?family=Maven+Pro:wght@400;500&family=PT+Serif:wght@700&display=swap">
<style>
:root{
  --header-bg:#2e2e2e;
  --header-light:#3a3a3a;
  --nav-bg:#3d3d3d;
  --nav-line:#262626;
  --nav-text:#e6e6e6;
  --accent:#f39b1c;
  --stage-bg:#8c8c8c;
  --page-bg:#dcdcdc;
  --content-bg:#f1f1f1;
  --text:#2a2a2a;
  --muted:#666;
  --link:#1a64c8;
  --box-border:#d6d6d6;
  --box-head:#e4e4e4;
  --button:#2c5fb0;
  --badge-green:#5a9a3b;
  --footer-bg:#2b2b2b;
  --footer-text:#9a9a9a;
}
*{box-sizing:border-box;margin:0;padding:0}
html,body{width:1200px;height:1047px;overflow:hidden}
body{font-family:"Maven Pro",Arial,sans-serif;background:var(--page-bg);color:var(--text);position:relative}
a{text-decoration:none;color:var(--link)}

.site-header{position:absolute;left:0;top:0;width:1200px;height:112px;
  background:radial-gradient(ellipse 500px 160px at 520px 20px,var(--header-light),var(--header-bg));}
.brand{position:absolute;left:189px;top:28px}
.brand-name{font-size:36px;font-weight:400;color:#e2e2e2;letter-spacing:1px;line-height:1}
.brand-tagline{font-size:12.5px;color:#8d8d8d;margin-top:7px;letter-spacing:.6px}
.header-contact{position:absolute;right:157px;top:66px;display:flex;align-items:center;gap:6px;color:#a8a8a8;font-size:14.5px;letter-spacing:.5px}
.header-contact svg{display:block}

.main-nav{position:absolute;left:0;top:112px;width:1200px;height:37px;background:linear-gradient(#474747,#353535);border-top:1px solid #555}
.main-nav ul{list-style:none;display:flex;position:absolute;left:158px;top:0;height:36px;border-left:1px solid var(--nav-line)}
.main-nav li{height:36px;padding:0 14px;display:flex;align-items:center;font-size:13px;color:var(--nav-text);border-right:1px solid var(--nav-line)}
.main-nav li.active{color:var(--accent)}
.main-nav .caret{display:inline-block;margin-left:7px;border:4px solid transparent;border-top:5px solid #9a9a9a;margin-top:4px}

.stage{position:absolute;left:0;top:149px;width:1200px;height:404px;background:var(--stage-bg)}
.slider-frame{position:absolute;left:159px;top:20px;width:885px;height:339px;background:#a9a9a9;border:1px solid #6e6e6e;border-radius:4px;box-shadow:0 14px 16px -8px rgba(0,0,0,.45)}
.slide{position:absolute;left:8px;top:7px;width:868px;height:323px;
  background:linear-gradient(180deg,#8fb6e4 0%,#c9dcef 22%,#c8a023 38%,#e0b81a 55%,#8a6a24 68%,#4f7fae 78%,#7a6540 92%,#6b4a2a 100%)}
.slider-dots{position:absolute;left:566px;top:378px;display:flex;gap:6px}
.slider-dots span{width:12px;height:12px;border-radius:50%;background:#777;border:1px solid #6a6a6a}
.slider-dots span.current{background:#eee;border-color:#bbb}

.content{position:absolute;left:158px;top:553px;width:886px;height:457px;background:var(--content-bg)}
.breadcrumb{position:absolute;left:21px;top:21px;font-size:12.5px;color:var(--muted);width:640px;padding-bottom:10px;border-bottom:1px dashed #d4d4d4}
.breadcrumb .sep{display:inline-block;border:3.5px solid transparent;border-left:4px solid var(--accent);margin:0 3px 0 6px}
.breadcrumb .current{color:var(--text)}
.page-title{position:absolute;left:14px;top:53px;width:660px;height:39px;background:linear-gradient(#f8f8f8,#dcdcdc);border:1px solid #d0d0d0;border-radius:3px;
  font-family:"PT Serif",Georgia,serif;font-weight:700;font-size:17.5px;color:#555;padding:10px 14px;letter-spacing:.3px}
.article{position:absolute;left:28px;top:99px;width:632px;font-size:12.6px;line-height:22.2px;text-align:justify;color:var(--text)}
.article p+p{margin-top:22px}

.sidebar-box{position:absolute;left:695px;width:170px;background:#f3f3f3;border:1px solid var(--box-border);border-radius:3px}
.sidebar-box h3{font-weight:400;font-size:12.5px;color:#444;background:var(--box-head);padding:8px 10px;letter-spacing:.3px;border-bottom:1px solid var(--box-border)}
.booking{top:14px;height:176px}
.booking form{padding:12px 11px 0 0}
.field{display:flex;justify-content:flex-end;align-items:center;gap:5px;font-size:11.5px;color:#555;letter-spacing:.4px;margin-bottom:6px}
.field .input{width:79px;height:19px;background:#fff;border:1px solid #aaa}
.field .select{height:18px;background:#fff;border:1px solid #aaa;display:flex;align-items:center;font-size:11.5px;color:#333;padding-left:8px;position:relative}
.field .select::after{content:"";position:absolute;right:1px;top:1px;width:14px;height:14px;background:#e8e8e8;border:1px solid #888}
.field .select.adults{width:42px;margin-right:38px}
.field .select.children{width:42px;margin-right:38px}
.submit{display:block;margin:10px auto 0 53px;width:78px;height:22px;border-radius:4px;background:linear-gradient(#4a7fd0,var(--button));color:#fff;font-size:12.5px;text-align:center;line-height:22px;border:1px solid #244f95}
.certificate{top:204px;height:194px}
.badge{margin:13px auto 0;width:140px;height:117px;background:#fff;border:1px solid #9bbf86;position:relative}
.badge .band{position:absolute;left:0;bottom:0;width:100%;height:18px;background:var(--badge-green)}
.tour-link{display:block;text-align:center;font-size:11.5px;line-height:13px;margin-top:5px}

.site-footer{position:absolute;left:0;top:1010px;width:1200px;height:37px;background:var(--footer-bg);color:var(--footer-text);font-size:12.5px;text-align:center;line-height:37px;letter-spacing:.3px}
</style>
</head>
<body>
<header class="site-header">
  <div class="brand">
    <div class="brand-name">Corwith Lodge</div>
    <div class="brand-tagline">Located in the heart of downtown Aspen</div>
  </div>
  <div class="header-contact">
    <svg width="15" height="15" viewBox="0 0 15 15" aria-label="Social page"><rect width="15" height="15" rx="2" fill="#4a78c4"/></svg>
    <svg width="16" height="15" viewBox="0 0 16 15" aria-label="Email"><rect x="1" y="2" width="14" height="11" rx="2" fill="none" stroke="#f39b1c" stroke-width="1.8"/><path d="M2 4l6 5 6-5" fill="none" stroke="#f39b1c" stroke-width="1.6"/></svg>
    <svg width="16" height="15" viewBox="0 0 16 15" aria-label="Phone"><rect x="1" y="5" width="14" height="9" rx="1.5" fill="#9a9a9a"/><path d="M3 5c0-3 10-3 10 0" fill="none" stroke="#9a9a9a" stroke-width="2"/><g fill="#2e2e2e"><rect x="4" y="7" width="2" height="2"/><rect x="7" y="7" width="2" height="2"/><rect x="10" y="7" width="2" height="2"/><rect x="4" y="10" width="2" height="2"/><rect x="7" y="10" width="2" height="2"/><rect x="10" y="10" width="2" height="2"/></g></svg>
    <span>970-555-0147</span>
  </div>
</header>

<nav class="main-nav">
  <ul>
    <li>Home</li>
    <li class="active">About The Lodge<span class="caret"></span></li>
    <li>Rooms<span class="caret"></span></li>
    <li>Reservations</li>
    <li>Amenities</li>
    <li>Aspen Information</li>
    <li>webcams</li>
    <li>contactUs</li>
  </ul>
</nav>

<section class="stage">
  <div class="slider-frame">
    <div class="slide" role="img" aria-label="Autumn aspen forest in golden colour around a calm mountain lake under a blue sky"></div>
  </div>
  <div class="slider-dots"><span class="current"></span><span></span><span></span><span></span></div>
</section>

<main class="content">
  <div class="breadcrumb">You are here: <a href="#">Home</a><span class="sep"></span><a href="#">About The Lodge</a><span class="sep"></span><span class="current">History of the Lodge</span></div>
  <h1 class="page-title">HISTORY OF THE LODGE</h1>
  <div class="article">
    <p>The Corwith Lodge was founded in 1948 and has been a local favorite ever since. It was originally known as the Hollyfield Lodge and was renamed in 2005. As a family-owned lodge, we take pride in maintaining a comfortable home away from home in beautiful Aspen, Colorado. The lodge has 35 guest rooms and each room is uniquely decorated with specially chosen furniture and tiles that give the feel of luxury. Every room has a a flat panel television with cable, high speed internet access via ethernet cable and via wireless connection, and CD player clock radios. Each morning of your stay you will be treated to a buffet breakfast that is included with your room. Then just walk outside and catch the free shuttle bus to Aspen Mountain or Snowmass. It’s a quick ride from our door to the Aspen Mountain Gondola.</p>
    <p>And after a long day of skiing, mountain biking, or hiking, you may relax in our hot tub with great views of Aspen Mountain and Red Mountain, or enjoy freshly baked cookies in front of our lobby fireplace or our courtyard firepit. Our staff will assist you in discovering all that Aspen has to offer from the best restaurants in town to great places for summer and winter activities. We look forward to seeing you at the Corwith Lodge, where every day is a holiday.</p>
  </div>

  <aside class="sidebar-box booking">
    <h3>Availability and Rates</h3>
    <form>
      <div class="field">Arrival:<span class="input"></span></div>
      <div class="field">Departure:<span class="input"></span></div>
      <div class="field">Adults:<span class="select adults">2</span></div>
      <div class="field">Children:<span class="select children"></span></div>
      <span class="submit">submit</span>
    </form>
  </aside>

  <aside class="sidebar-box certificate">
    <h3>Certificate</h3>
    <div class="badge" role="img" aria-label="Award certificate badge"><span class="band"></span></div>
    <a class="tour-link" href="#">Click here for a virtual tour<br>of the lodge!</a>
  </aside>
</main>

<footer class="site-footer">Copyright © 2004-2012 Corwith Lodge. All rights reserved.</footer>
</body>
</html>
```